Course Graduation Certificate

This project is not for a flyer but instead for the creation of a course graduation certificate. The final certificate needs to include the Marlowe Summit Aviation Academy logo and the text stating as follows:
Certifies that ___________________________ has satisfactorily completed the course of _______________________________ on ________________________________
I would also like to include some type of gold seal of completion as well as a place to sign my name and credentials at the bottom of the certificate
I have included the Marlowe Summit Aviation Academy logo as well as three other certificate examples for you to work from.
Target Market(s)
Students completing a certification course and receiving a certificate
Look and feel

```html
<!DOCTYPE html>
<html lang="en">
<head>
<meta charset="utf-8">
<title>Course Graduation Certificate – Marlowe Summit Aviation Academy</title>
<link rel="stylesheet" href="https://fonts.googleapis.com/css2?family=Libre+Baskerville:wght@400;700&family=Poppins:wght@400;600&display=swap">
<style>
  :root {
    --paper: #ffffff;
    --gold: #c9a437;
    --gold-light: #ecd98a;
    --gold-deep: #a8842a;
    --brand-blue: #1570f2;
    --ink: #111111;
    --rule: #3d4a52;
    --watermark: #eef4fd;
    --seal-navy: #1b3446;
  }
  html, body {
    margin: 0;
    padding: 0;
    width: 1200px;
    height: 927px;
    overflow: hidden;
    background: var(--paper);
  }
  .certificate {
    position: relative;
    width: 1200px;
    height: 927px;
    background: var(--paper);
    font-family: "Poppins", sans-serif;
    color: var(--ink);
  }
  .frame {
    position: absolute;
    inset: 0;
  }
  .academy-name {
    position: absolute;
    top: 118px;
    left: 0;
    width: 1200px;
    text-align: center;
    margin: 0;
    font-family: "Poppins", sans-serif;
    font-weight: 600;
    font-size: 26px;
    letter-spacing: 1px;
    color: var(--brand-blue);
  }
  .academy-watermark {
    position: absolute;
    top: 455px;
    left: 0;
    width: 1200px;
    text-align: center;
    margin: 0;
    font-family: "Poppins", sans-serif;
    font-weight: 600;
    font-size: 62px;
    line-height: 1.15;
    color: var(--watermark);
  }
  .title {
    position: absolute;
    top: 176px;
    left: 0;
    width: 1200px;
    margin: 0;
    text-align: center;
    font-family: "Libre Baskerville", serif;
    font-weight: 700;
    font-size: 84px;
    line-height: 1;
    color: var(--brand-blue);
  }
  .subtitle {
    position: absolute;
    top: 290px;
    left: 0;
    width: 1200px;
    margin: 0;
    text-align: center;
    font-family: "Libre Baskerville", serif;
    font-weight: 400;
    font-size: 35px;
    line-height: 1;
    color: var(--ink);
  }
  .statement {
    position: absolute;
    margin: 0;
    font-size: 30px;
    line-height: 1;
    color: var(--ink);
  }
  .blank {
    position: absolute;
    height: 0;
    border-top: 1.5px solid var(--rule);
  }
  .signature-label {
    position: absolute;
    margin: 0;
    font-size: 18px;
    line-height: 1;
    color: var(--brand-blue);
  }
  .signature-line {
    position: absolute;
    top: 740px;
    width: 278px;
    height: 0;
    border-top: 2px dashed var(--rule);
  }
  .seal {
    position: absolute;
    left: 515px;
    top: 680px;
    width: 168px;
    height: 168px;
  }
  .serial {
    position: absolute;
    left: 1111px;
    top: 844px;
    margin: 0;
    font-size: 21px;
    line-height: 1;
    color: var(--ink);
  }
</style>
</head>
<body>
<main class="certificate">
  <svg class="frame" width="1200" height="927" viewBox="0 0 1200 927" aria-hidden="false">
    <defs>
      <linearGradient id="goldTone" x1="0" y1="0" x2="1" y2="1">
        <stop offset="0" stop-color="#b8912e"/>
        <stop offset="0.5" stop-color="#e4cc78"/>
        <stop offset="1" stop-color="#b08a2a"/>
      </linearGradient>
    </defs>
    <!-- outer thin border -->
    <rect x="20" y="18" width="1160" height="891" fill="none" stroke="var(--gold)" stroke-width="1.5"/>
    <!-- top and bottom double bands -->
    <line x1="195" y1="26" x2="1005" y2="26" stroke="var(--gold)" stroke-width="2"/>
    <line x1="195" y1="56" x2="1005" y2="56" stroke="var(--gold)" stroke-width="3"/>
    <line x1="195" y1="901" x2="1005" y2="901" stroke="var(--gold)" stroke-width="2"/>
    <line x1="195" y1="871" x2="1005" y2="871" stroke="var(--gold)" stroke-width="3"/>
    <!-- side double bands -->
    <line x1="29" y1="195" x2="29" y2="732" stroke="var(--gold)" stroke-width="2"/>
    <line x1="58" y1="195" x2="58" y2="732" stroke="var(--gold)" stroke-width="3"/>
    <line x1="1171" y1="195" x2="1171" y2="732" stroke="var(--gold)" stroke-width="2"/>
    <line x1="1142" y1="195" x2="1142" y2="732" stroke="var(--gold)" stroke-width="3"/>
    <!-- inner corner curves -->
    <path d="M58 195 Q170 170 195 56" fill="none" stroke="var(--gold)" stroke-width="2"/>
    <path d="M1142 195 Q1030 170 1005 56" fill="none" stroke="var(--gold)" stroke-width="2"/>
    <path d="M58 732 Q170 757 195 871" fill="none" stroke="var(--gold)" stroke-width="2"/>
    <path d="M1142 732 Q1030 757 1005 871" fill="none" stroke="var(--gold)" stroke-width="2"/>
    <!-- corner ornaments -->
    <path role="img" aria-label="Gold filigree corner ornament" d="M18 16 H190 Q178 100 130 140 Q90 175 18 190 Z" fill="url(#goldTone)" opacity="0.85"/>
    <path role="img" aria-label="Gold filigree corner ornament" d="M1182 16 H1010 Q1022 100 1070 140 Q1110 175 1182 190 Z" fill="url(#goldTone)" opacity="0.85"/>
    <path role="img" aria-label="Gold filigree corner ornament" d="M18 911 H190 Q178 827 130 787 Q90 752 18 737 Z" fill="url(#goldTone)" opacity="0.85"/>
    <path role="img" aria-label="Gold filigree corner ornament" d="M1182 911 H1010 Q1022 827 1070 787 Q1110 752 1182 737 Z" fill="url(#goldTone)" opacity="0.85"/>
  </svg>

  <p class="academy-watermark" aria-hidden="true">Marlowe Summit<br>Aviation Academy</p>

  <p class="academy-name">Marlowe Summit Aviation Academy</p>

  <h1 class="title">Certificate</h1>
  <p class="subtitle">Of Course Graduation</p>

  <p class="statement" style="left:167px; top:385px;">Certifies that</p>
  <div class="blank" style="left:384px; top:413px; width:571px;"></div>
  <p class="statement" style="left:974px; top:385px;">has</p>

  <p class="statement" style="left:0; width:1200px; text-align:center; top:446px;">satisfactorily completed the course of</p>

  <div class="blank" style="left:245px; top:530px; width:669px;"></div>
  <p class="statement" style="left:925px; top:507px;">on</p>

  <div class="blank" style="left:245px; top:596px; width:706px;"></div>

  <p class="signature-label" style="left:193px; top:699px;">CEO’S Signature And Seal</p>
  <div class="signature-line" style="left:172px;"></div>

  <svg class="seal" viewBox="0 0 168 168" role="img" aria-label="Gold seal of completion">
    <defs>
      <radialGradient id="sealGold" cx="0.4" cy="0.35" r="0.7">
        <stop offset="0" stop-color="#f3e08f"/>
        <stop offset="1" stop-color="#c08a2c"/>
      </radialGradient>
    </defs>
    <circle cx="84" cy="84" r="82" fill="url(#sealGold)"/>
    <circle cx="84" cy="84" r="70" fill="var(--seal-navy)"/>
  </svg>

  <p class="signature-label" style="left:812px; top:700px;">Trainer’s Signature</p>
  <div class="signature-line" style="left:761px;"></div>

  <p class="serial">C60</p>
</main>
</body>
</html>
```